Christmas Postcard a manufacturer of skirting boards

Relaunch of the Christmas greetings Postcard of a company manufacturing premium quality skirting boards from real wood. Please refer to http://www.brumholt-profile.example/

- Christmas greetings Postcard 105 mm x 210 mm (card will be sent without envelope)

frontside:
- your graphic design, including
- Logo on the card
- Greetings "Frohe Weihnachten und ein erfolgreiches neues Jahr" on the card (front)
- insert Wooden Earring(s) - for recognition!

backside: (on the left)
"Wir bedanken uns für die partnerschaftliche Zusammenarbeit und freuen uns darauf, Sie auch im Jahr 2016 mit unseren Angeboten, Ideen und Know-how bei der Verwirklichung Ihrer Vorhaben zu unterstützen. (see pdf´s)

Ihnen und Ihren Mitarbeitern wünschen wir ein zauberhaftes Weihnachtsfest und für das neue Jahr Gesundheit, Glück, Erfolg und Freude."

Signatures (see pdf`s)

backside (on the right):
Adress field

------
The pdf´s from last years are just for the color mood. Fresh, modern design appreciated, no comic style.

Industry/Entity Type

It Company

Requirements
Must have
• "Wooden Earring(s)"

```html
<!DOCTYPE html>
<html lang="de">
<head>
<meta charset="utf-8">
<title>Brumholt Profile – Weihnachtskarte</title>
<link rel="stylesheet" href="https://fonts.googleapis.com/css2?family=Cormorant+Garamond:ital,wght@1,500&display=swap">
<style>
  :root {
    --paper: #fcf8fb;
    --wine: #8b0f22;
    --gold-light: #f3d37a;
    --gold: #c9962d;
    --gold-dark: #8a5a14;
    --wood-light: #f0c98a;
    --wood: #d9a55c;
    --lace: #b9808a;
  }
  html, body {
    margin: 0;
    padding: 0;
    width: 1200px;
    height: 2400px;
    overflow: hidden;
    background: var(--paper);
  }
  .card {
    position: relative;
    width: 1200px;
    height: 2400px;
    background: var(--paper);
    font-family: "Cormorant Garamond", Georgia, serif;
  }
  .snowflake {
    position: absolute;
    width: 168px;
    height: 188px;
    border-radius: 50%;
    background: radial-gradient(circle, var(--gold-light) 0%, var(--gold) 45%, rgba(201,150,45,0) 72%);
  }
  .snowflake--top { left: 500px; top: 47px; }
  .snowflake--bottom { left: 521px; top: 2090px; }

  .brand {
    position: absolute;
    left: 400px;
    top: 272px;
    width: 371px;
    height: 115px;
    display: flex;
    align-items: center;
    justify-content: center;
    gap: 18px;
  }
  .brand__mark {
    width: 34px;
    height: 34px;
    background: var(--wine);
  }
  .brand__name {
    font-size: 58px;
    font-style: italic;
    font-weight: 500;
    color: var(--wine);
    line-height: 1;
  }

  .border-band {
    position: absolute;
    left: 0;
    width: 1200px;
  }
  .border-band--top { top: 461px; height: 56px; }
  .border-band--bottom { top: 1896px; left: 13px; width: 1187px; height: 60px; }
  .border-band__lace {
    position: absolute;
    left: 0;
    top: 0;
    width: 100%;
    height: 62%;
    background: linear-gradient(180deg, rgba(185,128,138,0.15), rgba(185,128,138,0.45), rgba(185,128,138,0.15));
  }
  .border-band__rail {
    position: absolute;
    left: 0;
    bottom: 0;
    width: 100%;
    height: 14px;
    background: linear-gradient(180deg, var(--gold-light), var(--gold) 50%, var(--gold-dark));
  }

  .wooden-earring {
    position: absolute;
    left: 1117px;
    top: 515px;
    width: 38px;
    height: 183px;
    background: linear-gradient(90deg, var(--wood), var(--wood-light) 50%, var(--wood));
  }

  .greeting {
    position: absolute;
    left: 0;
    top: 755px;
    width: 1200px;
    margin: 0;
    text-align: center;
    font-size: 84px;
    font-style: italic;
    font-weight: 500;
    line-height: 112px;
    color: var(--wine);
  }

  .sleigh {
    position: absolute;
    left: 128px;
    top: 1232px;
    width: 944px;
    height: 576px;
    border-radius: 120px 200px 60px 60px;
    background: radial-gradient(ellipse at 45% 45%, var(--wine) 0%, var(--wine) 45%, var(--gold) 75%, rgba(201,150,45,0) 100%);
  }
</style>
</head>
<body>
  <main class="card">
    <div class="snowflake snowflake--top" role="img" aria-label="Goldene Schneeflocke als Schmuckelement"></div>

    <div class="brand">
      <span class="brand__mark"></span>
      <span class="brand__name">Brumholt Profile</span>
    </div>

    <div class="border-band border-band--top">
      <div class="border-band__lace" role="img" aria-label="Zierbordüre aus verschlungenen Schleifen"></div>
      <div class="border-band__rail"></div>
    </div>

    <div class="wooden-earring" role="img" aria-label="Hölzerner Anhänger aus Echtholzleiste"></div>

    <p class="greeting">"Frohe Weihnachten und ein<br>erfolgreiches neues Jahr"</p>

    <div class="sleigh" role="img" aria-label="Roter Schlitten mit goldenen, geschwungenen Kufen"></div>

    <div class="border-band border-band--bottom">
      <div class="border-band__lace" role="img" aria-label="Zierbordüre aus verschlungenen Schleifen"></div>
      <div class="border-band__rail"></div>
    </div>

    <div class="snowflake snowflake--bottom" role="img" aria-label="Goldene Schneeflocke als Schmuckelement"></div>
  </main>
</body>
</html>
```